Business Card Ayurvedic Massage

I'm starting with my ayurvedic massage business and need a business card design. The design should be inline with my brand/logo as well as with the design of my website (www.lumo-thara.ch).
Front: logo and text "Ayurvedische Massagen"
back: name and adress (see details https://www.lumo-thara.ch/kontakt.html)

```html
<!DOCTYPE html>
<html lang="de">
<head>
<meta charset="utf-8">
<title>lumo-thara – Visitenkarte</title>
<link rel="stylesheet" href="https://fonts.googleapis.com/css2?family=Gentium+Book+Plus:ital,wght@0,400;0,700;1,400&display=swap">
<style>
  :root {
    --artboard: #646464;
    --red-bright: #a80405;
    --red-mid: #7a0002;
    --red-dark: #3f0000;
    --gold: #e8c36a;
    --gold-deep: #c9973a;
    --gold-line: #f4d68e;
    --ink-light: #ffffff;
    --amber-light: #b8742e;
    --amber-dark: #6a3412;
  }
  * { margin: 0; padding: 0; box-sizing: border-box; }
  html, body {
    width: 1200px; height: 902px; overflow: hidden;
    background: var(--artboard);
    font-family: "Gentium Book Plus", Georgia, serif;
  }
  .artboard { position: relative; width: 1200px; height: 902px; }
  .card {
    position: absolute; top: 108px; width: 462px; height: 757px;
    background:
      radial-gradient(ellipse 75% 60% at 5% 55%, var(--red-bright) 0%, var(--red-mid) 45%, transparent 80%),
      linear-gradient(160deg, var(--red-mid) 0%, #5c0001 55%, var(--red-dark) 100%);
    border: 1px solid #8a8a8a;
    overflow: hidden;
  }
  .card--front { left: 78px; }
  .card--back { left: 599px; border-color: #3a0000; }

  .gold-rule {
    position: absolute; left: 0; width: 100%; height: 2px;
    background: linear-gradient(90deg, var(--gold-deep), var(--gold-line) 50%, var(--gold-deep));
  }
  .gold-rule--t1 { top: 32px; } .gold-rule--t2 { top: 46px; }
  .gold-rule--b1 { top: 702px; } .gold-rule--b2 { top: 716px; }

  .brand-name, .brand-tagline, .person-name, .person-role {
    position: absolute; left: 0; width: 100%;
    text-align: center; color: var(--gold); line-height: 1; white-space: nowrap;
  }
  .brand-name { top: 333px; font-size: 26px; letter-spacing: 1px; }
  .brand-tagline { top: 401px; font-size: 34px; }

  .person-name { top: 118px; font-size: 45px; }
  .person-role { top: 164px; font-size: 28px; font-style: italic; }

  .contact-list { list-style: none; }
  .contact-item {
    position: absolute; left: 84px; height: 22px; width: 370px;
    color: var(--ink-light); font-size: 18px; font-weight: 700; line-height: 22px; white-space: nowrap;
  }
  .contact-item svg { position: absolute; left: 0; top: 0; width: 22px; height: 22px; fill: var(--ink-light); }
  .contact-item span { position: absolute; top: 0; }
  .contact-item--address { top: 261px; } .contact-item--address span { left: 33px; }
  .contact-item--email { top: 306px; } .contact-item--email span { left: 41px; }
  .contact-item--phone { top: 355px; } .contact-item--phone span { left: 57px; }
  .contact-item--web { top: 394px; } .contact-item--web span { left: 53px; }

  .lamps-placeholder {
    position: absolute; left: 57px; top: 568px; width: 344px; height: 112px;
    border-radius: 6px;
    background: linear-gradient(180deg, var(--amber-light) 0%, var(--amber-dark) 100%);
  }
</style>
</head>
<body>
<main class="artboard">
  <section class="card card--front" aria-label="Vorderseite">
    <div class="gold-rule gold-rule--t1"></div>
    <div class="gold-rule gold-rule--t2"></div>
    <p class="brand-name">lumo-thara</p>
    <p class="brand-tagline">Ayurvedische Massagen</p>
    <div class="gold-rule gold-rule--b1"></div>
    <div class="gold-rule gold-rule--b2"></div>
  </section>

  <section class="card card--back" aria-label="Rückseite">
    <h1 class="person-name" style="font-weight:400">Anselm Verdi</h1>
    <p class="person-role">Graphic Design</p>
    <ul class="contact-list">
      <li class="contact-item contact-item--address">
        <svg viewBox="0 0 24 24" aria-hidden="true"><path d="M12 1a8 8 0 0 0-8 8c0 6 8 14 8 14s8-8 8-14a8 8 0 0 0-8-8zm0 11a3 3 0 1 1 0-6 3 3 0 0 1 0 6z"/></svg>
        <span>45 Lindenweg, Bern, Switzerland</span>
      </li>
      <li class="contact-item contact-item--email">
        <svg viewBox="0 0 24 24" aria-hidden="true"><path d="M2 9l10-6 10 6v11H2zm2 1.5V18h16v-7.5l-8 5z"/></svg>
        <span>hallo@lumo-thara.ch</span>
      </li>
      <li class="contact-item contact-item--phone">
        <svg viewBox="0 0 24 24" aria-hidden="true"><path d="M6.6 10.8a15 15 0 0 0 6.6 6.6l2.2-2.2a1 1 0 0 1 1-.25 11 11 0 0 0 3.6.6 1 1 0 0 1 1 1V20a1 1 0 0 1-1 1A17 17 0 0 1 3 4a1 1 0 0 1 1-1h3.5a1 1 0 0 1 1 1 11 11 0 0 0 .6 3.6 1 1 0 0 1-.25 1z"/></svg>
        <span>+41 31 555 01 23</span>
      </li>
      <li class="contact-item contact-item--web">
        <svg viewBox="0 0 24 24" aria-hidden="true"><path d="M6 2l13 12h-6.5l3.5 7-2.6 1.2-3.5-7.2L6 19.5z"/></svg>
        <span>www.lumo-thara.ch</span>
      </li>
    </ul>
    <div class="lamps-placeholder" role="img" aria-label="Illustration: five glowing clay oil lamps (diyas) in a row"></div>
  </section>
</main>
</body>
</html>
```